Card design for Heating and Cooling company

this is for a heating and cooling company we recently updated our logo and need to update our cards. We attached our logo so you can incorporate it into the card. We specialize in residential and commercial furnace and air condition repairs. Have been in business since 2014.

Phone number 555.284.9137

We need the following phrases
:Repairs, Installations, and maintenance
:Quality work at reasonable prices
:residential/commercial
:Licensed &Insured
:Email Pinegrovehvac47@mailbox-example.com
Name: Teodor K (Ted)
Also on back side I would like my logo with wording :Thank you for your business and refferal

Industry/Entity Type

Hvac

Contact Information for Business Card

:residential/commercial
:Licensed & Insured
Name: Teodor K (Ted)
Number:555.284.9136

Requirements
Must have
• Blue and red colors
Nice to have
• Maybe a pic of a furnace or air conditioner

```html
<!DOCTYPE html>
<html lang="en">
<head>
<meta charset="utf-8">
<title>Pinegrove Heating &amp; Cooling – Business Card</title>
<link href="https://fonts.googleapis.com/css2?family=Arimo:wght@400;700&display=swap" rel="stylesheet">
<style>
  :root {
    --bg: #e6e7ea;
    --card: #ffffff;
    --red: #ff0000;
    --sky: #0aa5ee;
    --navy: #1414d2;
    --ink: #111111;
    --font: "Arimo", Arial, sans-serif;
  }
  * { box-sizing: border-box; margin: 0; padding: 0; }
  html, body { width: 1200px; height: 1200px; overflow: hidden; }
  body { background: var(--bg); font-family: var(--font); position: relative; }

  .card {
    position: absolute;
    left: 160px;
    width: 880px;
    height: 500px;
    background: var(--card);
    box-shadow: 0 6px 24px rgba(0,0,0,.18);
    overflow: hidden;
  }
  .card--front { top: 70px; }
  .card--back  { top: 630px; }

  .card__shapes { position: absolute; inset: 0; }

  .brand {
    position: absolute;
    display: flex;
    align-items: center;
    gap: 10px;
    color: var(--ink);
    font-weight: 700;
    letter-spacing: 1px;
    white-space: nowrap;
  }
  .brand__dot { border-radius: 50%; background: var(--sky); flex: none; }
  .card--front .brand { left: 44px; top: 90px; font-size: 26px; }
  .card--front .brand__dot { width: 28px; height: 28px; }

  .owner { position: absolute; left: 48px; top: 320px; color: var(--sky); white-space: nowrap; }
  .owner__name { font-size: 38px; font-weight: 700; letter-spacing: 1px; }
  .owner__role { font-size: 25px; margin-top: -4px; }

  .contact { position: absolute; left: 350px; top: 95px; color: var(--navy); font-size: 19px; white-space: nowrap; }
  .contact__row { display: flex; align-items: center; gap: 14px; margin-bottom: 22px; }
  .contact__icon { width: 34px; height: 34px; flex: none; }
  .contact__rule { width: 340px; height: 4px; background: var(--red); margin-top: 18px; }

  .services { position: absolute; left: 340px; top: 300px; color: var(--navy); font-size: 20px; line-height: 1.6; list-style: none; white-space: nowrap; }

  .card--back .brand { left: 50%; top: 150px; transform: translateX(-50%); font-size: 56px; gap: 18px; }
  .card--back .brand__dot { width: 60px; height: 60px; }
  .thanks {
    position: absolute; left: 0; right: 0; bottom: 70px;
    text-align: center; color: var(--navy); font-size: 34px;
  }
</style>
</head>
<body>

<section class="card card--front">
  <svg class="card__shapes" viewBox="0 0 880 500" aria-hidden="true">
    <path d="M250 0 Q 360 250 240 500" fill="none" stroke="var(--red)" stroke-width="6"/>
    <path d="M770 0 Q 860 250 720 500 L 880 500 L 880 0 Z" fill="var(--red)"/>
  </svg>

  <div class="brand"><span class="brand__dot"></span>PINEGROVE</div>

  <div class="owner">
    <p class="owner__name">TEODOR K</p>
    <p class="owner__role">Owner</p>
  </div>

  <div class="contact">
    <div class="contact__row">
      <svg class="contact__icon" viewBox="0 0 36 36" aria-hidden="true">
        <circle cx="18" cy="18" r="18" fill="var(--red)"/>
        <path d="M12 9c1-1 2.5-1 3 0l2 4c.4 1 0 1.7-.7 2.3l-1.2 1c.9 2 2.6 3.7 4.6 4.6l1-1.2c.6-.7 1.3-1.1 2.3-.7l4 2c1 .5 1 2 0 3l-1.5 1.5c-1.5 1.5-5 .8-9-3.2S9 13 10.5 10.5z" fill="#fff"/>
      </svg>
      <span>555.284.9137</span>
    </div>
    <div class="contact__row">
      <svg class="contact__icon" viewBox="0 0 36 36" aria-hidden="true">
        <rect x="2" y="7" width="32" height="22" fill="none" stroke="var(--red)" stroke-width="3"/>
        <path d="M2 7 L18 20 L34 7 M2 29 L14 17 M34 29 L22 17" fill="none" stroke="var(--red)" stroke-width="3"/>
      </svg>
      <span>Pinegrovehvac47@mailbox-example.com</span>
    </div>
    <div class="contact__rule"></div>
  </div>

  <ul class="services">
    <li>Repairs, Installations, and maintenance</li>
    <li>Quality work at reasonable prices</li>
    <li>Residential/commercial</li>
    <li>Licensed &amp;Insured</li>
  </ul>
</section>

<section class="card card--back">
  <div class="brand"><span class="brand__dot"></span>PINEGROVE</div>
  <p class="thanks">Thank you for your business and refferal</p>
</section>

</body>
</html>
```